Cloud Based Internet Protection Service Business Cards

I would like a professionally designed business card. I already have a logo which I have attached.

The business is an online cloud based internet protection service aimed parents, particularly at non-technical parents and also schools.

The card should be be quite simple in its design, not to full of text and give its information in a clear and concise manner

Target Market(s)

Parents (especially non-technical parents) and also schools

Industry/Entity Type

Internet

Colors

Designer to choose colors to be used in the design.

Requirements
Should not have
• Too much text or be too cluttered. No decorative fonts, just a clear and concise font.

```html
<!DOCTYPE html>
<html lang="en">
<head>
<meta charset="utf-8">
<title>Kinshield Business Card</title>
<link rel="stylesheet" href="https://fonts.googleapis.com/css2?family=Lobster&family=Open+Sans:wght@400;700&family=PT+Sans+Narrow:wght@400;700&display=swap">
<style>
  :root {
    --backdrop: #5a0a0e;
    --card: #f6f6f6;
    --red: #d0112b;
    --band-grey: #ebebeb;
    --ink: #555555;
    --brand-blue: #1f4a6b;
    --white: #ffffff;
  }
  * { margin: 0; padding: 0; box-sizing: border-box; }
  html, body { width: 1200px; height: 970px; overflow: hidden; }
  body {
    background: var(--backdrop);
    position: relative;
    font-family: "Open Sans", Arial, sans-serif;
  }
  .card {
    position: absolute;
    background: var(--card);
    box-shadow: 0 6px 24px rgba(0,0,0,.45);
    overflow: hidden;
  }
  .card-front { left: 88px; top: 102px; width: 459px; height: 796px; }
  .card-back { left: 660px; top: 102px; width: 477px; height: 795px; }

  .brand-mark {
    position: absolute;
    display: flex;
    align-items: center;
    gap: 14px;
    color: var(--brand-blue);
    font-family: "Open Sans", Arial, sans-serif;
    font-weight: 700;
    letter-spacing: 2px;
  }
  .brand-mark .dot {
    border-radius: 50%;
    background: var(--brand-blue);
    flex: none;
  }
  .card-front .brand-mark { left: 52px; top: 322px; font-size: 46px; }
  .card-front .brand-mark .dot { width: 64px; height: 64px; }
  .card-back .brand-mark { left: 66px; top: 412px; font-size: 34px; }
  .card-back .brand-mark .dot { width: 48px; height: 48px; }

  .slogan-shade {
    position: absolute; left: 0; top: 471px; width: 407px; height: 80px;
    background: var(--band-grey);
  }
  .name-band {
    position: absolute; left: 51px; top: 433px; width: 408px; height: 80px;
    background: var(--red);
    color: var(--white);
    font-family: "Lobster", cursive;
    font-size: 58px;
    line-height: 80px;
    text-align: center;
  }
  .slogan {
    position: absolute; left: 0; top: 520px; width: 407px;
    text-align: center;
    font-family: "PT Sans Narrow", Arial, sans-serif;
    font-size: 17px;
    color: var(--ink);
  }

  .side-stripe {
    position: absolute; left: 0; width: 52px; background: var(--red);
  }
  .side-stripe.upper { top: 0; height: 501px; }
  .side-stripe.lower { top: 718px; height: 77px; }

  .person-band {
    position: absolute; left: 176px; top: 119px; width: 301px; height: 55px;
    background: var(--red);
    color: var(--white);
    font-family: "PT Sans Narrow", Arial, sans-serif;
    font-weight: 700;
    font-size: 36px;
    line-height: 55px;
    text-align: center;
    padding-right: 52px;
  }
  .designation {
    position: absolute; left: 176px; top: 178px; width: 248px;
    text-align: center;
    font-size: 20px;
    color: var(--ink);
  }

  .contact-list { list-style: none; }
  .contact-row {
    position: absolute; left: 0; width: 423px; height: 48px;
    background: var(--band-grey);
    display: flex; align-items: center;
    padding-left: 66px;
    font-size: 19px;
    color: var(--ink);
  }
  .contact-row svg { width: 16px; height: 16px; margin-right: 21px; flex: none; }
  .row-address { top: 503px; }
  .row-phone { top: 559px; }
  .row-email { top: 615px; }
  .row-web { top: 671px; }
</style>
</head>
<body>

<section class="card card-front">
  <div class="brand-mark"><span class="dot"></span>KINSHIELD</div>
  <div class="slogan-shade"></div>
  <div class="name-band">Kinshield</div>
  <p class="slogan">“slogan goes here”</p>
</section>

<section class="card card-back">
  <div class="side-stripe upper"></div>
  <div class="side-stripe lower"></div>
  <div class="person-band">Your Name</div>
  <p class="designation">Designation</p>
  <div class="brand-mark"><span class="dot"></span>KINSHIELD</div>

  <ul class="contact-list">
    <li class="contact-row row-address">
      <svg viewBox="0 0 16 16"><path d="M8 1a5 5 0 0 0-5 5c0 4 5 9 5 9s5-5 5-9a5 5 0 0 0-5-5zm0 7a2 2 0 1 1 0-4 2 2 0 0 1 0 4z" fill="#d0112b"/></svg>
      Your Address Goes Here
    </li>
    <li class="contact-row row-phone">
      <svg viewBox="0 0 16 16"><path d="M5 2h3v3H6.5v6H8v3H5a1 1 0 0 1-1-1V3a1 1 0 0 1 1-1z" fill="#d0112b"/></svg>
      +1 (234) 567890
    </li>
    <li class="contact-row row-email">
      <svg viewBox="0 0 16 16"><rect x="1.5" y="3.5" width="13" height="9" fill="none" stroke="#d0112b" stroke-width="1.4"/><path d="M1.5 3.5 8 9l6.5-5.5" fill="none" stroke="#d0112b" stroke-width="1.4"/></svg>
      info@kinshield.com
    </li>
    <li class="contact-row row-web">
      <svg viewBox="0 0 16 16" fill="none" stroke="#d0112b" stroke-width="1.3"><circle cx="8" cy="8" r="6.5"/><ellipse cx="8" cy="8" rx="3" ry="6.5"/><path d="M1.5 8h13M2.5 4.8h11M2.5 11.2h11"/></svg>
      www.kinshield.com
    </li>
  </ul>
</section>

</body>
</html>
```